Lumen Systems New Website - IT Infrastructure | Smart Cabinet | Micro Data Center

We're an IT SI providing Server Room Design & Build | All-in-One Rack & Smart Cabinet | Structured Cabling | IT Relocation | Maintenance. Old website can be found at www.lumensys-demo.com.hk. We'd like a brand new wix website which is modern, minimalist, interactive with some animation. Website content will be mostly static and include our service, our project, news and events, about us, contacts, blogs, partners and brands, etc.

reference sites:
We'd like to see more designs referring to below

https://www.pixelbidhub.example/design/40517736
https://www.pixelbidhub.example/design/40592214
https://velbrix.example/

Animation (scrolling effect) referring to
https://velbrix.example/intelligence/smart-office-room/
Updates

we'd like below style.

Designs look the same

Target Market(s)

Commercials in HK

Industry/Entity Type

IT, Technology, Data Center

Coding

Coded - Design and coding required

Font styles to use
Sans Serif

Requirements
Must have
• CMS, Some Interactive Elements/ Graphics

```html
<!DOCTYPE html>
<html lang="en">
<head>
<meta charset="utf-8">
<title>Lumen Systems – IT Infrastructure Solutions</title>
<link rel="stylesheet" href="https://fonts.googleapis.com/css2?family=Heebo:wght@400;500;700&family=Lato:wght@400;700&display=swap">
<style>
:root{
  --red:#d63a26;
  --navy:#141b33;
  --navy-deep:#0f1530;
  --footer:#16181d;
  --grey-bg:#f3f3f4;
  --card-grey:#f1f1f1;
  --ink:#1e2230;
  --muted:#6b6f78;
  --white:#ffffff;
}
*{box-sizing:border-box;margin:0;padding:0}
html,body{width:1200px;height:4804px;overflow:hidden}
body{position:relative;background:var(--white);font-family:"Lato",sans-serif;color:var(--ink)}
.abs{position:absolute}
.heading{font-family:"Heebo",sans-serif;font-weight:700;color:var(--ink);font-size:36px;line-height:1.2}
.heading .accent{color:var(--red)}
.center{left:0;width:1200px;text-align:center}
.tag{font-size:9px;color:var(--ink);padding-left:6px;border-left:2px solid var(--red);line-height:11px;display:inline-block}
.tag.light{color:#cfd3dd}
.btn{display:flex;align-items:center;justify-content:center;font-family:"Lato",sans-serif;font-weight:700;font-size:10px;color:var(--white);background:var(--red)}
.btn.outline{background:transparent;color:var(--red);border:1px solid var(--red);font-weight:400}

.hero{top:0;left:0;width:1200px;height:580px;background:linear-gradient(100deg,#1b2240 0%,#202a55 40%,#2b3668 70%,#1c2344 100%)}
.hero-shape{top:0;left:0}
.brand{display:flex;align-items:center;gap:8px;font-family:"Lato",sans-serif;font-weight:700;color:var(--white);font-size:22px}
.brand .mark{width:20px;height:20px;border:2px solid var(--white)}
.nav{font-size:12px;color:var(--white)}
.nav a{color:var(--white);text-decoration:none;position:absolute;white-space:nowrap}
.hero-title{top:202px;left:150px;font-size:37px;color:var(--white);line-height:50px}
.hero-text{top:312px;left:150px;width:470px;font-size:11.5px;line-height:18px;color:#dfe3ee}

.feature{position:absolute;width:340px;height:90px}
.feature .icon{position:absolute;left:0;top:0;width:88px;height:88px}
.feature h3{position:absolute;left:100px;top:2px;font-family:"Lato",sans-serif;font-weight:700;font-size:13px;color:var(--ink)}
.feature p{position:absolute;left:100px;top:24px;width:230px;font-size:10px;line-height:15px;color:var(--muted)}

.service{position:absolute;top:1300px;width:254px;height:143px;background:var(--card-grey);padding:30px 40px}
.service .num{font-family:"Heebo",sans-serif;font-size:28px;color:var(--red);line-height:1}
.service .label{margin-top:20px;font-size:13px;line-height:21px;color:#45494f}
.service.active{background:var(--red)}
.service.active .num,.service.active .label{color:var(--white)}
.service.active .label{font-weight:700}

.about-text{top:1690px;left:627px;width:330px;font-size:11.5px;line-height:19px;color:#dde1ea}
.ticks{top:1856px;left:630px;list-style:none}
.ticks li{height:24px;display:flex;align-items:center;gap:14px;font-size:10.5px;color:#c9cdd8}
.ticks svg{flex:none}

.project{position:absolute;top:2329px;width:196px;height:213px;background:var(--white);box-shadow:0 1px 3px rgba(0,0,0,.08)}
.project.raised{box-shadow:0 6px 16px rgba(0,0,0,.14)}
.project .photo{height:103px;background:linear-gradient(180deg,#2d3552 0%,#4a5470 55%,#8b93a6 100%)}
.project h4{padding:12px 11px 0;height:58px;font-family:"Lato",sans-serif;font-weight:400;font-size:13.5px;line-height:21px;color:#3a3d44}
.project .btn{margin:12px 11px 0;height:30px;font-size:10px}

.post{position:absolute;left:369px;width:462px;height:160px}
.post .photo{position:absolute;left:0;top:0;width:148px;height:147px;background:linear-gradient(180deg,#2a3250 0%,#515b77 50%,#9aa1b1 100%)}
.post .body{position:absolute;left:167px;top:18px;width:290px}
.post .date{font-size:9px;color:#8a8e96}
.post h4{margin-top:8px;font-family:"Lato",sans-serif;font-weight:400;font-size:14px;color:var(--ink)}
.post p{margin-top:8px;font-size:10px;line-height:15px;color:var(--muted)}
.post .more{display:block;margin-top:9px;font-size:10px;color:var(--red)}
.rule{position:absolute;left:369px;width:462px;height:1px;background:#c9cbd0}

.partner{position:absolute;top:3572px;width:180px;text-align:center;font-family:"Heebo",sans-serif;font-weight:700;font-size:22px;color:#8e9096;letter-spacing:1px}

.field{position:absolute;left:640px;width:327px;border:1px solid #c7cad3;font-size:10px;color:var(--white);padding:12px 14px}

.foot-title{font-family:"Lato",sans-serif;font-weight:700;font-size:11px;color:var(--white)}
.foot-link{font-size:9.5px;line-height:14px;color:#c4c7ce}
.social{width:14px;height:14px;border-radius:50%;background:var(--white)}
</style>
</head>
<body>

<section class="abs hero" role="img" aria-label="Dimly lit data center aisle with rows of server racks in deep blue light"></section>
<svg class="abs hero-shape" width="1200" height="1160" viewBox="0 0 1200 1160" style="top:0">
  <polygon points="0,576 300,505 1200,572 1200,1100 0,1155" fill="var(--grey-bg)"/>
</svg>

<div class="abs brand" style="top:38px;left:160px"><span class="mark"></span>Lumen Systems</div>
<nav class="abs nav" style="left:0;top:44px;width:1200px">
  <a href="#" style="left:697px;color:var(--red)">Home</a>
  <a href="#" style="left:771px">About</a>
  <a href="#" style="left:847px">Pages</a>
  <a href="#" style="left:922px">Project</a>
  <a href="#" style="left:1004px">Contact</a>
</nav>
<span class="abs tag light" style="top:186px;left:151px;color:#e6e8ef">The #Best Technical Solutions Provider</span>
<h1 class="abs heading hero-title">Design Your IT Infrastructure<br>Solution with the Best</h1>
<p class="abs hero-text">We deliver the best in Data Center Infrastructure, Network Infrastructure, Structured Cabling, Telephony, Access Control, Video Surveillance, Audiovisual &amp; Conferencing, Relocation &amp; Migration and Maintenance solutions.</p>
<a class="abs btn" style="top:398px;left:151px;width:128px;height:36px">Explore More</a>

<div class="abs center" style="top:626px"><span class="tag">What We Do</span></div>
<h2 class="abs heading center" style="top:644px">Why We <span class="accent">Special</span></h2>

<div class="feature" style="top:744px;left:274px">
  <svg class="icon" viewBox="0 0 88 88"><circle cx="44" cy="44" r="42" fill="none" stroke="#2a2d36" stroke-width="1.5"/><circle cx="44" cy="40" r="13" fill="none" stroke="#2a2d36" stroke-width="1.5"/><rect x="38" y="54" width="12" height="8" fill="none" stroke="#2a2d36" stroke-width="1.5"/><circle cx="44" cy="40" r="5" fill="none" stroke="var(--red)" stroke-width="1.8"/><path d="M44 20v-5M26 40h-5M62 40h5M31 27l-4-4M57 27l4-4" stroke="var(--red)" stroke-width="1.5"/></svg>
  <h3>Comprehensive Expertise</h3>
  <p>Lorem ipsum dolor sit amet, consectetur adipiscing elit. Amet proin ut vitae, felis. Mauris aliquet faucibus iaculis dui vitae ullamcorper ac.</p>
</div>
<div class="feature" style="top:744px;left:624px">
  <svg class="icon" viewBox="0 0 88 88"><circle cx="44" cy="44" r="42" fill="none" stroke="#2a2d36" stroke-width="1.5"/><path d="M22 48l12-12 10 6 10-6 12 12-10 10-12-8-12 8z" fill="none" stroke="#2a2d36" stroke-width="1.5"/><circle cx="44" cy="28" r="8" fill="none" stroke="var(--red)" stroke-width="1.5"/><path d="M40 28l3 3 5-6" fill="none" stroke="var(--red)" stroke-width="1.5"/></svg>
  <h3>Recognition &amp; Trust</h3>
  <p>Lorem ipsum dolor sit amet, consectetur adipiscing elit. Amet proin ut vitae, felis. Mauris aliquet faucibus iaculis dui vitae ullamcorper ac</p>
</div>
<div class="feature" style="top:871px;left:274px">
  <svg class="icon" viewBox="0 0 88 88"><circle cx="44" cy="44" r="42" fill="none" stroke="#2a2d36" stroke-width="1.5"/><path d="M20 40v22l14 6M68 40v22l-14 6" fill="none" stroke="#2a2d36" stroke-width="1.5"/><circle cx="44" cy="40" r="13" fill="none" stroke="var(--red)" stroke-width="1.5"/><path d="M44 32v16M48 35h-6a2.5 2.5 0 0 0 0 5h4a2.5 2.5 0 0 1 0 5h-6" fill="none" stroke="var(--red)" stroke-width="1.5"/></svg>
  <h3>Cost-Effective Solutions</h3>
  <p>Lorem ipsum dolor sit amet, consectetur adipiscing elit. Amet proin ut vitae, felis. Mauris aliquet faucibus iaculis dui vitae ullamcorper ac.</p>
</div>
<div class="feature" style="top:871px;left:624px">
  <svg class="icon" viewBox="0 0 88 88"><circle cx="44" cy="44" r="42" fill="none" stroke="#2a2d36" stroke-width="1.5"/><circle cx="44" cy="28" r="5" fill="none" stroke="var(--red)" stroke-width="1.5"/><circle cx="28" cy="54" r="5" fill="none" stroke="#2a2d36" stroke-width="1.5"/><circle cx="60" cy="54" r="5" fill="none" stroke="#2a2d36" stroke-width="1.5"/><circle cx="44" cy="46" r="8" fill="none" stroke="#2a2d36" stroke-width="1.5"/><path d="M40 33l-9 16M48 33l9 16M34 56h20" stroke="#2a2d36" stroke-width="1.2"/></svg>
  <h3>Dedicated &amp; Supportive Team</h3>
  <p>Lorem ipsum dolor sit amet, consectetur adipiscing elit. Amet proin ut vitae, felis. Mauris aliquet faucibus iaculis dui vitae ullamcorper ac</p>
</div>

<div class="abs center" style="top:1195px"><span class="tag">What We Do</span></div>
<h2 class="abs heading center" style="top:1213px">Our Services</h2>

<div class="service active" style="left:84px">
  <svg class="abs" style="top:44px;left:196px" width="40" height="10" viewBox="0 0 40 10"><path d="M0 5h38M33 1l4 4-4 4" fill="none" stroke="#fff" stroke-width="1.3"/></svg>
  <div class="num">01.</div>
  <div class="label">Data Center Design &amp;<br>Build</div>
</div>
<div class="service" style="left:343px"><div class="num">02.</div><div class="label">Structured cabling &amp;<br>fiber backbone</div></div>
<div class="service" style="left:602px"><div class="num">03.</div><div class="label">All-In-One Rack /<br>Micro-Data Center</div></div>
<div class="service" style="left:861px"><div class="num">04.</div><div class="label">Audiovisual and<br>Conference Room</div></div>

<svg class="abs" style="top:1540px;left:0" width="1200" height="620" viewBox="0 0 1200 620">
  <polygon points="0,75 896,5 1200,32 1200,620 0,620" fill="var(--navy)"/>
</svg>
<span class="abs tag light" style="top:1654px;left:244px">Who We Are</span>
<h2 class="abs heading" style="top:1672px;left:244px;color:var(--white);line-height:50px">About<br><span class="accent">Lumen</span> Systems</h2>
<p class="abs about-text">We deliver the best in Data Center Infrastructure, Network Infrastructure, Structured Cabling, Telephony, Access Control, Video Surveillance, Audiovisual &amp; Conferencing, Relocation &amp; Migration and Maintenance solutions.</p>
<div class="abs" role="img" aria-label="Miniature workers in hard hats repairing a network cable plug" style="top:1823px;left:244px;width:258px;height:248px;background:linear-gradient(135deg,#a7adb7 0%,#c9cdd3 45%,#8b6c3d 75%,#5e6470 100%)"></div>
<p class="abs" style="top:1822px;left:627px;font-size:12.5px;font-weight:700;color:var(--white)">LUMEN's solution at-a-glance includes:</p>
<ul class="abs ticks">
  <li><svg width="10" height="8" viewBox="0 0 10 8"><path d="M1 4l3 3 5-6" fill="none" stroke="var(--red)" stroke-width="1.5"/></svg>Data Center / Server Room Design and Build</li>
  <li><svg width="10" height="8" viewBox="0 0 10 8"><path d="M1 4l3 3 5-6" fill="none" stroke="var(--red)" stroke-width="1.5"/></svg>Structured Cabling Solution</li>
  <li><svg width="10" height="8" viewBox="0 0 10 8"><path d="M1 4l3 3 5-6" fill="none" stroke="var(--red)" stroke-width="1.5"/></svg>Data and Voice Networks, IP-Telephony Solution</li>
  <li><svg width="10" height="8" viewBox="0 0 10 8"><path d="M1 4l3 3 5-6" fill="none" stroke="var(--red)" stroke-width="1.5"/></svg>WiFi Solution</li>
  <li><svg width="10" height="8" viewBox="0 0 10 8"><path d="M1 4l3 3 5-6" fill="none" stroke="var(--red)" stroke-width="1.5"/></svg>Relocation and Migration Service</li>
  <li><svg width="10" height="8" viewBox="0 0 10 8"><path d="M1 4l3 3 5-6" fill="none" stroke="var(--red)" stroke-width="1.5"/></svg>AV and Conference Room System</li>
</ul>
<a class="abs btn" style="top:2036px;left:627px;width:127px;height:33px">Explore More</a>

<div class="abs center" style="top:2223px"><span class="tag">What We Have Done</span></div>
<h2 class="abs heading center" style="top:2241px">Our <span class="accent">Projects</span></h2>

<div class="project" style="left:200px"><div class="photo" role="img" aria-label="Empty server room with raised floor"></div><h4>A renowned China based listed insurance company</h4><a class="btn outline">Explore More</a></div>
<div class="project raised" style="left:401px"><div class="photo" role="img" aria-label="Empty server room with raised floor"></div><h4>Global Outlets</h4><a class="btn">Explore More</a></div>
<div class="project" style="left:603px"><div class="photo" role="img" aria-label="Empty server room with raised floor"></div><h4>Harbor Capital &amp; Meridian Life</h4><a class="btn outline">Explore More</a></div>
<div class="project" style="left:804px"><div class="photo" role="img" aria-label="Empty server room with raised floor"></div><h4>A renowned China based Securities firm</h4><a class="btn outline">Explore More</a></div>

<svg class="abs" style="top:2550px;left:0;z-index:-1" width="1200" height="900" viewBox="0 0 1200 900">
  <polygon points="0,92 1200,4 1200,830 0,895" fill="var(--grey-bg)"/>
</svg>
<div class="abs center" style="top:2656px"><span class="tag">Our Blogs</span></div>
<h2 class="abs heading center" style="top:2674px">News &amp; Events</h2>

<article class="post" style="top:2773px"><div class="photo" role="img" aria-label="Server room interior"></div><div class="body"><div class="date">23 December 2023</div><h4>Title of the News or Event Post</h4><p>Lorem ipsum dolor sit amet, consectetur adipiscing elit. Amet proin ut vita, felis. Mauris aliquet faucibus iaculis dui vitae ullamcorper ac.</p><a class="more">Read More</a></div></article>
<div class="rule" style="top:2933px"></div>
<article class="post" style="top:2946px"><div class="photo" role="img" aria-label="Server room interior"></div><div class="body"><div class="date">23 December 2023</div><h4>Title of the News or Event Post</h4><p>Lorem ipsum dolor sit amet, consectetur adipiscing elit. Amet proin ut vita, felis. Mauris aliquet faucibus iaculis dui vitae ullamcorper ac.</p><a class="more">Read More</a></div></article>
<div class="rule" style="top:3105px"></div>
<article class="post" style="top:3118px"><div class="photo" role="img" aria-label="Server room interior"></div><div class="body"><div class="date">23 December 2023</div><h4>Title of the News or Event Post</h4><p>Lorem ipsum dolor sit amet, consectetur adipiscing elit. Amet proin ut vita, felis. Mauris aliquet faucibus iaculis dui vitae ullamcorper ac.</p><a class="more">Read More</a></div></article>
<a class="abs btn" style="top:3305px;left:551px;width:98px;height:36px">View All</a>

<div class="abs center" style="top:3475px"><span class="tag">Featured In</span></div>
<h2 class="abs heading center" style="top:3493px">Our <span class="accent">Partners</span></h2>
<div class="partner" style="left:130px">Quorvane</div>
<div class="partner" style="left:321px">Threllix</div>
<div class="partner" style="left:516px">Marnoquist</div>
<div class="partner" style="left:714px">Zevantro</div>
<div class="partner" style="left:895px">Obrilux</div>
<a class="abs btn outline" style="top:3644px;left:551px;width:98px;height:36px">View All</a>

<div class="abs" style="top:3743px;left:0;width:1200px;height:720px;background:var(--navy-deep)"></div>
<span class="abs tag light" style="top:3796px;left:233px">Contact Us</span>
<h2 class="abs heading" style="top:3814px;left:233px;color:var(--white);line-height:50px">Get in Touch<br>with Us</h2>
<p class="abs" style="top:3846px;left:640px;width:330px;font-size:11.5px;line-height:19px;color:#dde1ea">Lorem ipsum dolor sit amet, consectetur adipiscing elit. Amet proin ut vitae, felis. Mauris aliquet faucibus iaculis dui vitae ullamcorper ac</p>
<svg class="abs" style="top:3945px;left:233px" width="26" height="26" viewBox="0 0 26 26"><circle cx="13" cy="13" r="13" fill="#fff"/><path d="M13 6a4.5 4.5 0 0 0-4.5 4.5c0 3.4 4.5 8.5 4.5 8.5s4.5-5.1 4.5-8.5A4.5 4.5 0 0 0 13 6z" fill="var(--navy-deep)"/><circle cx="13" cy="10.5" r="1.6" fill="#fff"/></svg>
<p class="abs" style="top:3946px;left:276px;width:250px;font-size:9px;line-height:12px;color:#dde1ea">Rm 905, 9/F, Nova Trade Centre, 18 Lantern Street, San Po Kong, Kowloon, Hong Kong</p>
<div class="abs" role="img" aria-label="Street map showing the office location" style="top:3999px;left:233px;width:340px;height:213px;background:linear-gradient(135deg,#e8ebe3 0%,#dfe6ee 50%,#e6e9e0 100%)"></div>

<div class="field" style="top:3939px;height:37px">Your name*</div>
<div class="field" style="top:3999px;height:37px">Email*</div>
<div class="field" style="top:4057px;height:37px">Subject*</div>
<div class="field" style="top:4115px;height:97px">Your Message</div>
<a class="abs btn" style="top:4234px;left:640px;width:96px;height:37px">Submit</a>

<svg class="abs" style="top:4440px;left:0" width="1200" height="364" viewBox="0 0 1200 364"><polygon points="0,14 1200,0 1200,364 0,364" fill="var(--footer)"/></svg>
<div class="abs brand" style="top:4522px;left:155px;font-size:22px"><span class="mark"></span>Lumen Systems</div>
<p class="abs foot-link" style="top:4584px;left:155px;width:195px">Lorem ipsum dolor sit amet consectetur. Mi nibh venenatis in suscipit turpis enim cursus vulputate amet, lobortis mi platea aliquam senectus tempus mauris neque.</p>
<div class="abs" style="top:4679px;left:155px;display:flex;gap:11px"><span class="social"></span><span class="social"></span><span class="social" style="border-radius:3px"></span></div>

<div class="abs foot-title" style="top:4514px;left:448px">Website Links</div>
<div class="abs foot-link" style="top:4552px;left:448px">Home</div>
<div class="abs foot-link" style="top:4587px;left:448px">About Us</div>
<div class="abs foot-link" style="top:4622px;left:448px">Our Projects</div>
<div class="abs foot-link" style="top:4656px;left:448px">FAQs</div>

<div class="abs foot-title" style="top:4514px;left:627px">Services</div>
<div class="abs foot-link" style="top:4548px;left:627px;width:130px">Website Data Center Design &amp; Build</div>
<div class="abs foot-link" style="top:4583px;left:627px;width:130px">Structured cabling and fiber backbone</div>
<div class="abs foot-link" style="top:4618px;left:627px;width:130px">All-In-One Rack / Micro-Data Center</div>
<div class="abs foot-link" style="top:4653px;left:627px;width:130px">Audiovisual and Conference Room</div>

<div class="abs foot-title" style="top:4514px;left:855px">Contact Us</div>
<svg class="abs" style="top:4568px;left:855px" width="10" height="13" viewBox="0 0 10 13"><path d="M5 0a4.5 4.5 0 0 0-4.5 4.5C.5 7.8 5 13 5 13s4.5-5.2 4.5-8.5A4.5 4.5 0 0 0 5 0z" fill="#fff"/><circle cx="5" cy="4.5" r="1.6" fill="var(--footer)"/></svg>
<div class="abs foot-link" style="top:4560px;left:883px;width:180px;font-size:9px;line-height:12px">Rm 905, 9/F, Nova Trade Centre, 18 Lantern Street, San Po Kong, Kowloon, Hong Kong</div>
<svg class="abs" style="top:4611px;left:855px" width="11" height="8" viewBox="0 0 11 8"><rect width="11" height="8" fill="#fff"/><path d="M0 0l5.5 4.5L11 0" fill="none" stroke="var(--footer)" stroke-width="1"/></svg>
<div class="abs foot-link" style="top:4608px;left:883px;font-size:9px">marketing@lumensys-demo.com.hk</div>
<svg class="abs" style="top:4644px;left:855px" width="10" height="10" viewBox="0 0 10 10"><path d="M2 0l2 2.5-1 1.5a6 6 0 0 0 3 3l1.5-1L10 8l-1.5 2C4 10 0 6 0 1.5z" fill="#fff"/></svg>
<div class="abs foot-link" style="top:4637px;left:883px;font-size:9px;line-height:12px">+852 2000 0100 /<br>+852 5000 0199</div>
<svg class="abs" style="top:4679px;left:855px" width="11" height="10" viewBox="0 0 11 10"><rect y="3" width="11" height="7" fill="#fff"/><rect x="2.5" width="6" height="4" fill="#fff"/></svg>
<div class="abs foot-link" style="top:4677px;left:883px;font-size:9px">+852 3000 0188</div>

<div class="abs" style="top:4740px;left:155px;width:895px;height:1px;background:#4a4d55"></div>
<div class="abs center foot-link" style="top:4772px;font-size:9px">Non Copyrighted © 2023 Lumen Systems Solutions</div>

</body>
</html>
```